Criação de Layout de Rótulo para Limpeza & Serviço para o lar
A empresa queria:
" ESTAMOS HÁ 42 ANOS FABRICANDO E VENDENDO OS MELHORES PRODUTOS DE LIMPEZA "

```html
<!DOCTYPE html>
<html lang="pt-BR">
<head>
<meta charset="UTF-8">
<title>Onda Viva – Aromatizador de ambiente Lavanda</title>
<link href="https://fonts.googleapis.com/css2?family=Montserrat:wght@400;500;600&family=DM+Serif+Display&family=Sacramento&display=swap" rel="stylesheet">
<style>
  :root {
    --canvas-bg: #f3f1f5;
    --label-bg: #fbfafc;
    --pattern-tint: #ece6f1;
    --band: #dacde7;
    --ink-strong: #7a5896;
    --ink: #8d6dab;
    --ink-soft: #9a80b4;
    --logo-dot: #b59ccc;
  }
  * { margin: 0; padding: 0; box-sizing: border-box; }
  html, body {
    width: 1200px;
    height: 1200px;
    overflow: hidden;
    background: var(--canvas-bg);
  }
  .label {
    position: absolute;
    left: 290px;
    top: 100px;
    width: 620px;
    height: 1000px;
    background: var(--label-bg);
    overflow: hidden;
    box-shadow: 0 10px 30px rgba(90, 60, 120, 0.08);
  }
  .label__pattern {
    position: absolute;
    inset: 0;
    background:
      radial-gradient(circle at 20% 30%, var(--pattern-tint) 0, transparent 45%),
      radial-gradient(circle at 80% 70%, var(--pattern-tint) 0, transparent 45%),
      linear-gradient(180deg, #faf8fb 0%, #f3eff6 100%);
  }
  .label__band {
    position: absolute;
    left: 120px;
    top: 0;
    width: 380px;
    height: 100%;
    background: var(--band);
  }
  .label__content {
    position: absolute;
    left: 120px;
    top: 0;
    width: 380px;
    text-align: center;
    color: var(--ink);
  }
  .brand {
    margin-top: 130px;
    display: flex;
    align-items: center;
    justify-content: center;
    gap: 14px;
  }
  .brand__dot {
    width: 16px;
    height: 16px;
    border-radius: 50%;
    background: var(--logo-dot);
  }
  .brand__name {
    font-family: "Montserrat", sans-serif;
    font-weight: 600;
    font-size: 54px;
    color: var(--ink-strong);
    letter-spacing: -0.5px;
  }
  .category {
    margin-top: 120px;
    font-family: "Montserrat", sans-serif;
    font-weight: 400;
    font-size: 27px;
    line-height: 1.25;
    color: var(--ink);
  }
  .product {
    margin-top: 48px;
    position: relative;
  }
  .product__name {
    font-family: "DM Serif Display", serif;
    font-size: 76px;
    line-height: 1;
    color: var(--ink-strong);
  }
  .product__script {
    display: block;
    margin-top: -14px;
    font-family: "Sacramento", cursive;
    font-size: 64px;
    line-height: 1;
    color: var(--ink-strong);
  }
  .product__type {
    display: block;
    margin-top: 2px;
    font-family: "Montserrat", sans-serif;
    font-weight: 500;
    font-size: 22px;
    letter-spacing: 6px;
    color: var(--ink-soft);
  }
  .fragrance {
    margin-top: 50px;
    font-family: "DM Serif Display", serif;
    font-size: 36px;
    color: var(--ink-strong);
  }
  .volume {
    margin-top: 46px;
    font-family: "Montserrat", sans-serif;
    font-weight: 400;
    font-size: 28px;
    color: var(--ink);
  }
</style>
</head>
<body>
  <main class="label">
    <div class="label__pattern" role="img" aria-label="Padrão floral delicado em linhas lilás claras sobre fundo branco"></div>
    <div class="label__band"></div>
    <div class="label__content">
      <div class="brand">
        <span class="brand__dot"></span>
        <span class="brand__name">Onda Viva</span>
      </div>
      <p class="category">Aromatizador<br>de ambiente</p>
      <div class="product">
        <h1 class="product__name">Brisa</h1>
        <span class="product__script">suave</span>
        <span class="product__type">HOME SPRAY</span>
      </div>
      <p class="fragrance">lavanda</p>
      <p class="volume">250ml</p>
    </div>
  </main>
</body>
</html>
```